TKA Electricial Contracting Services

Hi guys, after a design for my small electrical company, have logo design files to be incorporated into the layout, the basic concept is electrical contracting services for residential, commercial, industrial & data services, image is clean clear and strong,

Card format is to have a nice clean logo on front,with maybe the Residential – commercial – industrial - data, followed with licensed & insured, followed by contact details on backside of the card.

Target Market(s)

Residential, commercial, industrial sectors.

Industry/Entity Type

Electrical

Contact Information for Business Card

TKA logo,
Residential – commercial – industrial - data
REC: 61372
Email: tka@poralink.net.au
Phone: 0458 203 719

Requirements
Must have
• Clean & strong design.
Nice to have
• If possible, I would like the logo colours inverted so the text is orange and the background is black on the front of the card, then the backside of the card be the reverse colour
Should not have
• No Sparks, lightning bolts,

```html
<!DOCTYPE html>
<html lang="en">
<head>
<meta charset="utf-8">
<title>TKA Electrical Contracting Services – Business Card</title>
<link href="https://fonts.googleapis.com/css2?family=Exo+2:wght@700;800&family=Open+Sans:wght@400;600&display=swap" rel="stylesheet">
<style>
  :root {
    --orange: #f28a2e;
    --orange-deep: #e0701a;
    --black: #0c0c0c;
    --charcoal: #1b1b1b;
    --white: #ffffff;
    --page: #e9e6e2;
  }
  * { margin: 0; padding: 0; box-sizing: border-box; }
  html, body { width: 1200px; height: 900px; overflow: hidden; background: var(--page); }
  .stage { position: relative; width: 1200px; height: 900px; }

  .card {
    position: absolute; width: 640px; height: 372px; left: 280px;
    overflow: hidden; border-radius: 4px;
    box-shadow: 0 6px 18px rgba(0,0,0,.22);
  }

  /* ---------- Front ---------- */
  .card-front { top: 60px; background: linear-gradient(160deg, var(--orange) 0%, var(--orange-deep) 100%); }
  .front-bar { position: absolute; height: 9px; background: var(--black); }
  .front-bar.left { left: 0; top: 208px; width: 54px; }
  .front-bar.right { right: 0; top: 78px; width: 54px; }
  .front-brand { position: absolute; left: 0; right: 0; top: 56px; text-align: center; }
  .brand-name {
    font-family: "Exo 2", sans-serif; font-weight: 800; line-height: 1;
    letter-spacing: 2px;
  }
  .front-brand .brand-name { font-size: 112px; color: var(--black); }
  .brand-tagline {
    font-family: "Exo 2", sans-serif; font-weight: 700; font-size: 21px;
    letter-spacing: .5px; margin-top: 2px;
  }
  .front-brand .brand-tagline { color: var(--black); }
  .front-band {
    position: absolute; left: 0; right: 0; bottom: 0; height: 92px;
    background: var(--black); padding: 22px 32px 0 0; text-align: right;
    font-family: "Open Sans", sans-serif; font-weight: 600; font-size: 17px; line-height: 24px;
  }
  .front-band .licence { color: var(--orange); }
  .front-band .sectors { color: var(--white); }

  /* ---------- Back ---------- */
  .card-back { top: 468px; background: var(--black); }
  .back-shape { position: absolute; inset: 0; }
  .back-brand { position: absolute; left: 150px; top: 42px; }
  .back-brand .brand-name { font-size: 92px; color: var(--orange); }
  .back-brand .brand-tagline { color: var(--white); font-size: 18px; }
  .back-topbar { position: absolute; right: 0; top: 42px; width: 200px; height: 14px; background: var(--orange); }
  .holder { position: absolute; right: 42px; top: 150px; text-align: right; }
  .holder-name { font-family: "Exo 2", sans-serif; font-weight: 700; font-size: 26px; color: var(--orange); line-height: 1; }
  .holder-role { font-family: "Open Sans", sans-serif; font-size: 14px; color: var(--white); margin-top: 2px; }
  .holder-mark { position: absolute; right: 42px; top: 205px; width: 20px; height: 9px; background: var(--orange); }
  .divider { position: absolute; left: 150px; right: 62px; top: 212px; height: 1px; background: var(--white); transform: rotate(-4deg); transform-origin: right center; }
  .contact { position: absolute; left: 150px; top: 262px; font-family: "Open Sans", sans-serif; font-size: 19px; color: var(--orange); }
  .contact-mark { width: 40px; height: 9px; background: var(--orange); margin-bottom: 4px; }
  .contact-row { display: flex; align-items: center; gap: 10px; line-height: 26px; }
  .contact-row svg { width: 18px; height: 18px; flex: none; }
</style>
</head>
<body>
<main class="stage">

  <section class="card card-front" aria-label="Card front">
    <div class="front-bar right"></div>
    <div class="front-bar left"></div>
    <div class="front-brand">
      <div class="brand-name">TKA</div>
      <div class="brand-tagline">Tyler Kane Electrical</div>
    </div>
    <div class="front-band">
      <p class="licence">licenced &amp; insured Residential</p>
      <p class="sectors">commercial – industrial – data REC: 61372</p>
    </div>
  </section>

  <section class="card card-back" aria-label="Card back">
    <svg class="back-shape" viewBox="0 0 640 372" preserveAspectRatio="none" aria-hidden="true">
      <rect x="0" y="0" width="640" height="372" fill="var(--orange)"/>
      <path d="M58 0 C 78 60, 62 140, 82 230 C 92 300, 110 350, 150 372 L 640 372 L 640 0 Z" fill="var(--white)"/>
      <path d="M74 0 C 92 60, 78 140, 98 230 C 108 296, 124 340, 160 356 L 640 356 L 640 0 Z" fill="var(--black)"/>
      <rect x="160" y="356" width="140" height="16" fill="var(--white)"/>
      <rect x="300" y="356" width="110" height="16" fill="var(--orange)"/>
      <rect x="410" y="356" width="110" height="16" fill="var(--white)"/>
      <rect x="520" y="356" width="120" height="16" fill="var(--orange)"/>
    </svg>
    <div class="back-topbar"></div>
    <div class="back-brand">
      <div class="brand-name">TKA</div>
      <div class="brand-tagline">Tyler Kane Electrical</div>
    </div>
    <div class="holder">
      <div class="holder-name">Dana Hollis</div>
      <div class="holder-role">Owner</div>
    </div>
    <div class="holder-mark"></div>
    <div class="divider"></div>
    <div class="contact">
      <div class="contact-mark"></div>
      <div class="contact-row">
        <svg viewBox="0 0 24 24" aria-hidden="true"><path d="M6.6 10.8a15 15 0 0 0 6.6 6.6l2.2-2.2a1 1 0 0 1 1-.25 11 11 0 0 0 3.6.6 1 1 0 0 1 1 1V20a1 1 0 0 1-1 1A17 17 0 0 1 3 4a1 1 0 0 1 1-1h3.5a1 1 0 0 1 1 1 11 11 0 0 0 .6 3.6 1 1 0 0 1-.25 1z" fill="var(--white)"/></svg>
        <span>0458 203 719</span>
      </div>
      <div class="contact-row">
        <svg viewBox="0 0 24 24" aria-hidden="true"><rect x="2.5" y="5" width="19" height="14" rx="1" fill="none" stroke="var(--white)" stroke-width="1.8"/><path d="M3 6l9 7 9-7" fill="none" stroke="var(--white)" stroke-width="1.8"/></svg>
        <span>tka@poralink.net.au</span>
      </div>
    </div>
  </section>

</main>
</body>
</html>
```